Solvane Super Yacht Party Ibiza

PSD ONLY PROJECT
We need our first Website for brand new Super Yacht Party - Solvane.
We have some ideas on brand concepts and colours attached but are looking for something unique with a great layout and visually appealing.
We are looking for interesting ways to display and edit pictures - maybe with blur or watermark square over lays etc so the image is distorted somewhat.
Company Logo is attached and company font is Marquel Serif
Solvane the brand is aimed at the luxury market, this is for people who will spend 3 hours of their holiday partying on a super yacht, drinking champagne, easting Sushi, chilling on our VIP Beds and watching the sunset.
We are not looking for anything Nautical themed - so please no life buoys, stripes, portholes or wheels.
The website needs to ooze class and sophistication while also appealing to party hard music loving lubbers from Ibiza - this will be the tricky part to get right!
It needs to be visual and eye catching - we don't have any pre conceived ideas nessacarily so consider this a blank canvas.
I have added photos this project but if you have any others then please feel free to add them - don´t worry about watermarks we can remove them at a later stage.
Pages:
Homepage
The Yacht
VIP
Tickets [no page design necessary for tickets]
Contact
FAQ
Recruitment
HOMEPAGE:
The homepage needs to tell people about the event and give them instant affinity with the brand and what the party offers.
There needs to be a subscribe function for the newsletter.
There needs to be Social Feeds.
THE YACHT:
This needs to sell people to go on the Yacht they are going on see below for all points, needs to look luxurious and glamorous
VIP:
This needs to display the VIP options and encourage people to click to make an enquiry [handled through email]
CONTACT:
List of people to contact and company information - use any information for design stage
FAQ:
A list of common questions and answers displayed in a unique way copy provided at a later date.
RECRUITMENT:
Space for some copy about different jobs and click to apply handled through email
HOMEPAGE
The Ibiza boat party market is about to take a giant leap forward as 2015 sees the launch of brand new Super Yacht Event – Solvane.
Created by titans of the Ibiza boat and club scene with over 10 years experience the Solvane Super Yacht Parties will define a dawn of a new age for Ibiza Boat Parties where they are no longer confined to the top deck of a sight seeing catamaran.
Sailing exclusively from San Antonio in 2015, which is the only place to be seen capturing the islands iconic sunset. The San Antonio sunset has served as a backdrop for every major music revolution on the island and the Solvane Super Yacht Experience pulls no punches.
NOT ALL BOAT PARTIES ARE CREATED EQUAL
SUPER YACHT EXPERIENCE
ICONIC IBIZA SUNSET
4 FLOORS OF MUSIC
DEEP AND TECH HOUSE
KRELT SOUNDSYSTEM
VIP ROOMS AND BEDS AVAILABLE
ON BOARD LOCAL FASHION & MERCH SHOP
BOTTLE SERVICE TO TABLES
CHAMPAGNE SPRAY
€100 VODKA BOTTLE
WILDEST PARTY
HOTTEST GIRLS AND GUYS
ON BOARD HOT TUB
ISLANDS BEST ARIEL PRODUCTION AT SEA
VIP PAGE
Choose from
The ultimate in VIP on our luxury beds and in our themed rooms with full table service where everything is catered for.
Speak to our concierge team to make your reservation now.
TOP DECK BEDS
HOT TUB
MID DECK TABLES
UNDERWATER THEMED ROOMS
SUPER YACHT STATS
The Super Yacht has some impressive stats:
• The ultimate in VIP with full table service!
• Top Deck Beds with complimentary towels and Hot Tub!
• Underwater Rooms – secluded and themed with a private bed and window!
• Mid and Lower Deck Tables – in the heart of the action!
• 6 Luxury Toilets – no more long queues or nasty niffs!
• 4 Impressive Floors – There is space for everyone whether chilling or raving!
• 4 Premium Bars – don´t delay the party queuing for a drink!
• 1 Restaurant – Sushi, Finger Food and More from our on board Chefs.
• 1 Shop – Taking a break from the party? Local island trinkets with our own twist!
• 1 Brand New KRELT sound system – crystal clear sound to every floor with the finest Deep and Tech beats from our international resident team.
• The finest in production but not just limited to the boat as we fly in an International Water Stunt artist team to delight guests.
See following website for inspiration:
http://www.tidelornbay.com
http://www.varendocoastinn.com
http://www.pellowshore.com/destinations/beach-clubs/marbella/
http://www.bravintlounge.es
Any questions please let me know!!

```html
<!DOCTYPE html>
<html lang="en">
<head>
<meta charset="utf-8">
<title>Solvane Super Yacht Party Ibiza</title>
<link href="https://fonts.googleapis.com/css2?family=Raleway:wght@400;500;600;700&family=Open+Sans:wght@400;600;700;800&display=swap" rel="stylesheet">
<style>
  :root {
    --ink: #13161d;
    --gold: #a8913f;
    --gold-light: #bba654;
    --gold-dark: #93802f;
    --white: #ffffff;
    --text: #222222;
    --muted: #555555;
    --footer-muted: #b8b8b8;
  }
  * { margin: 0; padding: 0; box-sizing: border-box; }
  html, body { width: 1042px; height: 1200px; overflow: hidden; background: var(--white); }
  body { position: relative; font-family: "Open Sans", sans-serif; color: var(--text); }

  .topbar { position: absolute; left: 0; top: 0; width: 1042px; height: 69px; background: var(--ink); }
  .navband {
    position: absolute; left: 0; top: 69px; width: 1042px; height: 38px;
    background: linear-gradient(180deg, var(--gold-light), var(--gold-dark));
  }
  .nav { position: absolute; top: 0; height: 38px; display: flex; list-style: none; }
  .nav li {
    font-family: "Raleway", sans-serif; font-weight: 600; font-size: 12px; color: var(--white);
    line-height: 38px; padding: 0 13px; border-left: 1px solid rgba(0,0,0,0.12);
  }
  .nav li:first-child { border-left: none; }
  .nav-left { left: 155px; }
  .nav-right { left: 607px; }

  .brand {
    position: absolute; left: 437px; top: 7px; width: 150px; height: 150px; border-radius: 50%;
    background: var(--white); display: flex; align-items: center; justify-content: center; z-index: 3;
  }
  .brand-name { font-family: "Raleway", sans-serif; font-weight: 500; font-size: 26px; letter-spacing: 1px; color: var(--gold); }

  .hero {
    position: absolute; left: 0; top: 107px; width: 1042px; height: 437px;
    background: linear-gradient(180deg, #7d9ccb 0%, #a9bfd8 30%, #6f7e78 52%, #c9ccd0 66%, #3f5c83 72%, #2d4a77 100%);
  }
  .hero-arrow { position: absolute; top: 170px; }
  .hero-caption {
    position: absolute; left: 286px; top: 137px; width: 475px; height: 144px;
    background: rgba(20,22,30,0.88); border: 2px solid var(--white); text-align: center; color: var(--white);
  }
  .hero-title { font-family: "Open Sans", sans-serif; font-weight: 800; font-size: 31px; margin-top: 21px; letter-spacing: -0.3px; padding-left: 10px; }
  .hero-sub {
    font-family: "Open Sans", sans-serif; font-weight: 800; font-size: 20px; margin-top: 0; letter-spacing: -0.3px;
    color: var(--ink); -webkit-text-stroke: 1px var(--white);
  }
  .hero-text { font-size: 9px; line-height: 13px; color: #a9abb0; margin: 6px 34px 0; }

  .welcome { position: absolute; left: 0; top: 580px; width: 1042px; text-align: center; }
  .welcome h1 { font-family: "Raleway", sans-serif; font-weight: 500; font-size: 25px; color: #111; }
  .welcome .lead { font-size: 11.3px; margin-top: 10px; color: #222; }
  .welcome .body { font-size: 8.5px; line-height: 13.5px; width: 690px; margin: 8px auto 0; color: #333; }
  .tagline {
    position: absolute; left: 0; top: 705px; width: 1042px; text-align: center;
    font-family: "Raleway", sans-serif; font-weight: 500; font-size: 11px; color: #222;
  }
  .tagline svg { vertical-align: middle; margin: 0 4px; }

  .features { position: absolute; top: 741px; list-style: none; }
  .features li {
    font-family: "Raleway", sans-serif; font-weight: 500; font-size: 9.5px; color: var(--gold);
    height: 20px; padding-left: 10px; position: relative;
  }
  .features li::before {
    content: ""; position: absolute; left: 0; top: 3px;
    border-left: 3px solid #888; border-top: 3px solid transparent; border-bottom: 3px solid transparent;
  }
  .col-1 { left: 239px; } .col-2 { left: 408px; } .col-3 { left: 637px; }

  .highlight { position: absolute; top: 878px; width: 216px; height: 180px; }
  .highlight .photo {
    position: absolute; left: 25px; top: 2px; width: 164px; height: 164px; border-radius: 50%;
    border: 3px solid var(--white); box-shadow: 0 0 2px rgba(0,0,0,0.35);
  }
  .highlight .shadow {
    position: absolute; left: 30px; top: 163px; width: 155px; height: 12px; border-radius: 50%;
    background: radial-gradient(ellipse, rgba(0,0,0,0.25), rgba(0,0,0,0) 70%);
  }
  .highlight svg { position: absolute; left: 0; top: 99px; }
  .highlight .label {
    position: absolute; left: 28px; top: 110px; width: 160px; text-align: center;
    font-family: "Raleway", sans-serif; font-weight: 600; font-size: 13px; color: var(--white);
  }
  .h-yacht { left: 181px; } .h-ibiza { left: 414px; } .h-party { left: 647px; }
  .h-yacht .photo { background: linear-gradient(160deg, #d8e1ee 0%, #7d9bbf 40%, #4c6a5c 62%, #3a3f48 100%); }
  .h-ibiza .photo { background: radial-gradient(circle at 50% 55%, #fff3b0 0%, #f3b23a 22%, #d98a14 55%, #6b3a0c 100%); }
  .h-party .photo { background: linear-gradient(170deg, #f4ecd8 0%, #e3c7a3 45%, #c79a7b 70%, #5bb4d6 100%); }

  .footer { position: absolute; left: 0; top: 1105px; width: 1042px; height: 95px; background: var(--ink); border-top: 5px solid var(--gold); }
  .footer-nav { position: absolute; left: 162px; top: 24px; display: flex; list-style: none; }
  .footer-nav li { font-family: "Raleway", sans-serif; font-weight: 600; font-size: 10.5px; color: var(--white); margin-right: 25px; }
  .copyright { position: absolute; left: 161px; top: 52px; font-family: "Raleway", sans-serif; font-size: 8px; color: var(--footer-muted); }
  .social { position: absolute; left: 790px; top: 27px; display: flex; gap: 5px; }
  .social span { width: 18px; height: 18px; border-radius: 3px; background: var(--white); }
</style>
</head>
<body>
  <header>
    <div class="topbar"></div>
    <nav class="navband">
      <ul class="nav nav-left">
        <li>HOME</li><li>THE YACHT</li><li>VIP</li><li>TICKETS</li>
      </ul>
      <ul class="nav nav-right">
        <li>CONTACT</li><li>FAQ</li><li>RECRUITMENT</li>
      </ul>
    </nav>
    <div class="brand"><span class="brand-name">SOLVANE</span></div>
  </header>

  <section class="hero" role="img" aria-label="Photo of a white super yacht moored in Ibiza harbour with hills and town behind">
    <svg class="hero-arrow" style="left:138px" width="22" height="36" viewBox="0 0 22 36"><path d="M18 2 L4 18 L18 34" fill="none" stroke="#fff" stroke-width="4"/></svg>
    <svg class="hero-arrow" style="left:880px" width="22" height="36" viewBox="0 0 22 36"><path d="M4 2 L18 18 L4 34" fill="none" stroke="#fff" stroke-width="4"/></svg>
    <div class="hero-caption">
      <h2 class="hero-title">SUPER YACHT EXPERIENCE</h2>
      <p class="hero-sub">PRAESENT ELEMENTUM ELIT TELLUS</p>
      <p class="hero-text">Curabitur iaculis tempus eros Curabitur vel mi sit amet magna malesuada ultrices Ut nisi erat fermentum vel congue id euismod in elit Fusce ultricies orci ac</p>
    </div>
  </section>

  <main>
    <section class="welcome">
      <h1>WELCOME TO OUR WEBSITE MAINAPGE</h1>
      <p class="lead">The Ibiza boat party market is about to take a giant leap forward as 2015 sees the launch of brand new Super Yacht Event – Solvane.</p>
      <p class="body">Created by titans of the Ibiza boat and club scene with over 10 years experience the Solvane Super Yacht Parties will define a dawn of a new age for Ibiza Boat Parties where they are no longer confined to the top deck of a sight seeing catamaran. Sailing exclusively from San Antonio in 2015, which is the only place to be seen capturing the islands iconic sunset. The San Antonio sunset has served as a backdrop for every major music revolution on the island and the Solvane Super Yacht Experience pulls no punches.</p>
    </section>

    <p class="tagline">
      <svg width="26" height="8" viewBox="0 0 26 8"><path d="M1 5 Q7 1 13 4 T25 3" fill="none" stroke="#888" stroke-width="1"/></svg>NOT ALL BOAT PARTIES ARE CREATED EQUAL<svg width="26" height="8" viewBox="0 0 26 8"><path d="M1 3 Q7 7 13 4 T25 5" fill="none" stroke="#888" stroke-width="1"/></svg>
    </p>

    <ul class="features col-1">
      <li>SUPER YACHT EXPERIENCE</li><li>ICONIC IBIZA SUNSET</li><li>4 FLOORS OF MUSIC</li><li>DEEP AND TECH HOUSE</li><li>KRELT SOUNDSYSTEM</li>
    </ul>
    <ul class="features col-2">
      <li>VIP ROOMS AND BEDS AVAILABLE</li><li>ON BOARD LOCAL FASHION &amp; MERCH SHOP</li><li>BOTTLE SERVICE TO TABLES</li><li>CHAMPAGNE SPRAY</li><li>€100 VODKA BOTTLE</li>
    </ul>
    <ul class="features col-3">
      <li>WILDEST PARTY</li><li>HOTTEST GIRLS AND GUYS</li><li>ON BOARD HOT TUB</li><li>ISLANDS BEST ARIEL PRODUCTION AT SEA</li>
    </ul>

    <div class="highlight h-yacht">
      <div class="shadow"></div>
      <div class="photo" role="img" aria-label="Photo from the deck of a yacht at sea under a blue sky"></div>
      <svg width="216" height="40" viewBox="0 0 216 40"><path d="M0 3 L28 3 L28 37 L0 37 L14 20 Z M216 3 L188 3 L188 37 L216 37 L202 20 Z" fill="#9c8839"/><rect x="28" y="3" width="160" height="34" fill="#ad9744"/></svg>
      <span class="label">SUPER YACHT</span>
    </div>
    <div class="highlight h-ibiza">
      <div class="shadow"></div>
      <div class="photo" role="img" aria-label="Photo of hands forming a heart against an orange Ibiza sunset"></div>
      <svg width="216" height="40" viewBox="0 0 216 40"><path d="M0 3 L28 3 L28 37 L0 37 L14 20 Z M216 3 L188 3 L188 37 L216 37 L202 20 Z" fill="#9c8839"/><rect x="28" y="3" width="160" height="34" fill="#ad9744"/></svg>
      <span class="label">ICONIC IBIZA</span>
    </div>
    <div class="highlight h-party">
      <div class="shadow"></div>
      <div class="photo" role="img" aria-label="Photo of friends celebrating at a party by the water"></div>
      <svg width="216" height="40" viewBox="0 0 216 40"><path d="M0 3 L28 3 L28 37 L0 37 L14 20 Z M216 3 L188 3 L188 37 L216 37 L202 20 Z" fill="#9c8839"/><rect x="28" y="3" width="160" height="34" fill="#ad9744"/></svg>
      <span class="label">WILDEST PARTY</span>
    </div>
  </main>

  <footer class="footer">
    <ul class="footer-nav">
      <li>HOME</li><li>THE YACHT</li><li>VIP</li><li>TICKETS</li><li>CONTACT</li><li>FAQ</li><li>RECRUITMENT</li>
    </ul>
    <p class="copyright">© 2015 COMPANY NAME &nbsp;ALL RIGHT RESERVED &nbsp;TERM OF USE</p>
    <div class="social" aria-label="Social links"><span></span><span></span><span></span><span></span></div>
  </footer>
</body>
</html>
```